Health Care Service Company Flyer

Company name: Bright Harbor Clinic
Slogan: Find out what you're made of
Website: brightharborclinic.ca

I need the flyer to contain the company name (will provide logo source file ASAP), the slogan in large font and a "find out more at harborclinic.ca"

Other important data to include in the flyer is:
Four bullet points with the following information:
*Track performance and fitness results over time
*Develop proprietary exercise and dietary programs based on actionable data
*Track muscle atrophy from injury, as well as muscle gain during rehabilitation
*Reveal imbalances in muscle symmetry and strength, flexibility, and joint mechanics

I also need the following information conveyed somewhere on the flyer:
*Body Fat, Muscle Mass, and Bone Density Measurements
• Over 50 data points generated in each 10 minute scan
*Call XXX-XXX-XXX to book an appointment today

DEXA Body Composition Services.
Get scanned today.

See example of competitor flyers in the images to get an example of the images and information we are trying to convey

Target Market(s)

athletes, fitness enthusiast, crossfit

Industry/Entity Type

Health And Wellness

Colors
33a6d7
acd036

Requirements
Nice to have
• Prefer images be general health and wellness related - in other words, individuals who look healthy, but are not abnormally muscular
Should not have
• Shirtless models, No big muscles,

```html
<!DOCTYPE html>
<html lang="en">
<head>
<meta charset="utf-8">
<title>Bright Harbor Clinic – Flyer</title>
<link rel="stylesheet" href="https://fonts.googleapis.com/css2?family=Roboto:wght@400;500;700;900&family=Open+Sans:wght@400;600&display=swap">
<style>
  :root {
    --brand-blue: #33a6d7;
    --brand-green: #acd036;
    --ink: #2a2a2a;
    --paper: #ffffff;
    --backdrop: #e4e5e6;
  }
  * { box-sizing: border-box; margin: 0; padding: 0; }
  html, body { width: 1200px; height: 1200px; overflow: hidden; }
  body { background: var(--backdrop); font-family: "Roboto", Arial, sans-serif; }

  .flyer {
    position: absolute; left: 197px; top: 30px;
    width: 806px; height: 1140px;
    background: var(--paper);
    box-shadow: 0 6px 24px rgba(0,0,0,.18);
    overflow: hidden;
  }
  .flyer-art { position: absolute; inset: 0; }

  .brand-name {
    position: absolute; left: 40px; top: 36px;
    font-weight: 500; font-size: 58px; letter-spacing: 1px; line-height: 1;
    color: var(--brand-blue); text-transform: uppercase; white-space: nowrap;
  }
  .service-tag {
    position: absolute; left: 40px; top: 100px;
    background: var(--brand-green); color: #fff;
    font-weight: 700; font-size: 17px; padding: 3px 12px; white-space: nowrap;
  }

  .slogan {
    position: absolute; left: 40px; top: 490px;
    font-weight: 700; font-size: 28px; line-height: 1.1;
    color: var(--ink); white-space: nowrap;
  }

  .facility { position: absolute; left: 40px; top: 540px; width: 440px; }
  .facility-title {
    font-weight: 500; font-size: 36px; color: var(--brand-blue); margin-bottom: 10px;
  }
  .facility-list {
    list-style: none;
    font-family: "Open Sans", Arial, sans-serif; font-size: 15px;
    line-height: 1.35; color: var(--ink);
  }
  .facility-list li { position: relative; padding-left: 22px; margin-bottom: 10px; }
  .facility-list li::before {
    content: ""; position: absolute; left: 4px; top: 8px;
    width: 6px; height: 6px; border-radius: 50%; background: var(--ink);
  }

  .scan-stat {
    position: absolute; left: 598px; top: 680px; width: 204px;
    text-align: center; color: var(--ink);
    font-size: 25px; line-height: 1.18; font-weight: 400;
  }
  .scan-stat strong { font-weight: 900; }

  .dexa-note {
    position: absolute; left: 598px; top: 915px; width: 204px;
    text-align: center; color: #fff; font-size: 18px; line-height: 1.25;
  }
  .dexa-note strong { display: block; font-weight: 700; margin-bottom: 6px; }

  .booking { position: absolute; left: 60px; top: 1004px; color: #fff; }
  .booking-label { font-size: 22px; font-weight: 400; line-height: 1.2; }
  .booking-phone { font-size: 58px; font-weight: 500; line-height: 1.05; }
  .booking-site { font-size: 17px; font-weight: 400; line-height: 1.3; }
</style>
</head>
<body>
  <div class="flyer">
    <svg class="flyer-art" width="806" height="1140" viewBox="0 0 806 1140" xmlns="http://www.w3.org/2000/svg">
      <defs>
        <linearGradient id="gymTone" x1="0" y1="0" x2="1" y2="1">
          <stop offset="0" stop-color="#9aa3ab"/>
          <stop offset=".5" stop-color="#c9d0d6"/>
          <stop offset="1" stop-color="#6f7882"/>
        </linearGradient>
        <linearGradient id="warmTone" x1="0" y1="0" x2="1" y2="1">
          <stop offset="0" stop-color="#c9a27e"/>
          <stop offset="1" stop-color="#6b5446"/>
        </linearGradient>
        <linearGradient id="coolTone" x1="0" y1="0" x2="1" y2="1">
          <stop offset="0" stop-color="#8c9aa6"/>
          <stop offset="1" stop-color="#3f4a55"/>
        </linearGradient>
        <linearGradient id="brightTone" x1="0" y1="0" x2="1" y2="1">
          <stop offset="0" stop-color="#e0d6c8"/>
          <stop offset="1" stop-color="#b88aa0"/>
        </linearGradient>
        <linearGradient id="darkTone" x1="0" y1="0" x2="1" y2="1">
          <stop offset="0" stop-color="#3a2f33"/>
          <stop offset="1" stop-color="#1c1a1d"/>
        </linearGradient>
        <radialGradient id="stretchTone" cx=".5" cy=".55" r=".6">
          <stop offset="0" stop-color="#d79a86"/>
          <stop offset=".55" stop-color="#a45a8c"/>
          <stop offset="1" stop-color="#ffffff" stop-opacity="0"/>
        </radialGradient>
      </defs>

      <!-- green side column -->
      <polygon points="600,240 806,240 806,1140 560,1140" fill="var(--brand-green)"/>

      <!-- header rule -->
      <rect x="0" y="134" width="806" height="4" fill="var(--brand-green)"/>

      <!-- hero photo -->
      <g role="img" aria-label="Photo of a man and a woman training with battle ropes in a bright gym">
        <polygon points="0,140 806,140 806,200 0,470" fill="url(#gymTone)"/>
      </g>
      <line x1="0" y1="472" x2="806" y2="202" stroke="var(--brand-blue)" stroke-width="4"/>
      <line x1="0" y1="481" x2="806" y2="211" stroke="var(--brand-green)" stroke-width="3"/>

      <!-- activity tiles -->
      <g stroke="var(--brand-blue)" stroke-width="4">
        <rect role="img" aria-label="Photo of a group workout class" x="530" y="175" width="140" height="100" rx="14" fill="url(#warmTone)"/>
        <rect role="img" aria-label="Photo of a man doing a plank exercise" x="460" y="300" width="140" height="108" rx="14" fill="url(#coolTone)"/>
        <rect role="img" aria-label="Photo of women stretching in a fitness class" x="620" y="300" width="140" height="108" rx="14" fill="url(#brightTone)"/>
        <rect role="img" aria-label="Photo of a woman training with suspension straps" x="480" y="435" width="150" height="112" rx="14" fill="url(#coolTone)"/>
        <rect role="img" aria-label="Photo of a woman doing a barbell squat" x="650" y="435" width="140" height="112" rx="14" fill="url(#darkTone)"/>
      </g>

      <!-- stretching photo -->
      <g role="img" aria-label="Photo of a smiling woman in sportswear doing a seated leg stretch">
        <ellipse cx="360" cy="910" rx="220" ry="120" fill="url(#stretchTone)"/>
      </g>

      <!-- booking band -->
      <polygon points="0,1010 572,880 560,1140 0,1140" fill="var(--brand-blue)"/>
    </svg>

    <h1 class="brand-name">Bright Harbor Clinic</h1>
    <div class="service-tag">• Body Fat&nbsp; • Muscle Mass&nbsp; • Bone Density Measurements</div>

    <p class="slogan">Find out what you're made of</p>

    <section class="facility">
      <h2 class="facility-title">Facility</h2>
      <ul class="facility-list">
        <li>Track performance and fitness results over time</li>
        <li>Develop proprietary exercise and dietary programs based on actionable data</li>
        <li>Track muscle atrophy from injury, as well as muscle gain during rehabilitation</li>
        <li>Reveal imbalances in muscle symmetry and strength, flexibility, and joint mechanics</li>
      </ul>
    </section>

    <p class="scan-stat">Over<br><strong>50</strong> Data Points<br>Generated in Each<br><strong>10 minute</strong><br>Scan</p>

    <p class="dexa-note"><strong>DEXA Body Composition Services.</strong>Get scanned today.</p>

    <div class="booking">
      <p class="booking-label">Book an Appointment Today</p>
      <p class="booking-phone">(604) 555-0148</p>
      <p class="booking-site">Find out more at harborclinic.ca</p>
    </div>
  </div>
</body>
</html>
```